Landing Page IT Security Vendor

We need a landing page that uses our colour scheme (www.veldonguard.com). We created a draft (see attached). We do not need standard stock template design pages. Please only apply if you can design pages from scratch and try to be as close as possible to our draft. It is ok to also purchase commecrial stock pictures

Coding

Coded - Design and coding required

Number of Pages Required

1 page

```html
<!DOCTYPE html>
<html lang="en">
<head>
<meta charset="utf-8">
<title>Veldon Guard – Security Awareness Training</title>
<link href="https://fonts.googleapis.com/css2?family=Roboto:wght@300;400;500;700;900&family=Montserrat:wght@300;400;500&display=swap" rel="stylesheet">
<style>
:root{
  --orange:#f6a019;
  --orange-deep:#fb8a0c;
  --teal:#22bfcd;
  --teal-dark:#11a9b8;
  --navy:#0e2a38;
  --ink:#1b2530;
  --grey-band:#efefef;
  --white:#ffffff;
}
*{margin:0;padding:0;box-sizing:border-box}
html,body{width:1200px;height:2625px;overflow:hidden}
body{position:relative;font-family:"Roboto",Arial,sans-serif;color:var(--ink);background:var(--white)}
.abs{position:absolute}
/* top bar */
.topbar{left:0;top:0;width:1200px;height:60px;background:var(--orange);color:var(--white)}
.award{top:13px;display:flex;align-items:center;gap:10px;font-size:10.5px;font-weight:700;line-height:13px;white-space:nowrap}
.award .ico{width:22px;height:22px;border:2px solid rgba(255,255,255,.8);border-radius:50%;flex:none}
.topbar .divider{left:944px;top:10px;width:1px;height:40px;background:rgba(255,255,255,.8)}
.nav{top:19px;font-size:16px;font-weight:700}
/* hero */
.hero{left:0;top:60px;width:1200px;height:1177px;background:linear-gradient(180deg,#27c2d1 0%,#22bccb 60%,#1fb7c6 100%);overflow:hidden}
.hero .kicker{left:63px;top:138px;font-size:31px;font-weight:300;color:var(--white);letter-spacing:.2px;white-space:nowrap}
.hero h1{left:63px;top:222px;font-size:46px;line-height:57px;font-weight:900;color:var(--white);white-space:nowrap;letter-spacing:-.3px}
.btn{display:flex;align-items:center;justify-content:center;color:var(--white);font-weight:700;text-transform:uppercase;border-radius:32px;background:linear-gradient(180deg,var(--orange) 0%,var(--orange-deep) 100%);box-shadow:0 6px 0 rgba(246,160,25,.35);white-space:nowrap}
.hero .demo{left:63px;top:452px;width:255px;height:62px;font-size:21px}
.ring-outline{left:675px;top:15px;width:690px;height:690px;border:2px solid #53e2ee;border-radius:50%}
.ring{left:700px;top:20px;width:680px;height:680px;border-radius:50%;background:var(--orange)}
.photo{left:730px;top:45px;width:530px;height:530px;border-radius:50%;border:3px solid #3fd6e3;
  background:
    radial-gradient(ellipse 34% 42% at 62% 30%,rgba(70,150,200,.85) 0%,rgba(40,100,150,.55) 45%,rgba(20,60,95,0) 100%),
    radial-gradient(ellipse 55% 30% at 40% 72%,rgba(190,170,165,.55) 0%,rgba(120,120,135,.25) 55%,rgba(20,40,60,0) 100%),
    linear-gradient(170deg,#1d5a80 0%,#133c5c 45%,#0c2338 75%,#07121f 100%)}
.hero h2{left:0;top:665px;width:1200px;text-align:center;font-size:37px;font-weight:700;color:var(--white)}
.card{top:735px;width:341px;height:388px;background:var(--white);border-radius:34px;overflow:hidden}
.card .inner{padding:42px 16px 0 31px}
.card h3{font-size:19.5px;line-height:24px;font-weight:700;text-transform:uppercase;color:var(--ink)}
.card .lead{margin-top:24px;font-size:18.5px;line-height:22px;font-weight:500}
.card p{margin-top:24px;font-size:15px;line-height:22px;font-weight:400}
.card.tight h3{font-size:19px}
.card.tight .lead{margin-top:14px}
.card.tight p{margin-top:14px}
.card .btn{position:absolute;left:0;bottom:0;width:100%;height:62px;border-radius:0 0 34px 34px;font-size:19px;box-shadow:none}
/* MSSP band */
.band{left:0;top:1237px;width:1200px;height:145px;background:var(--grey-band)}
.band .txt{left:182px;top:51px;font-size:31px;font-weight:700;color:var(--navy);white-space:nowrap}
.band .more{left:790px;top:45px;width:178px;height:52px;border-radius:28px;background:var(--navy);color:var(--white);font-size:18px;font-weight:700;display:flex;align-items:center;justify-content:center;box-shadow:0 4px 0 rgba(14,42,56,.25)}
/* trust */
.trust{left:0;top:1426px;width:1200px;text-align:center;font-size:32px;line-height:44px;font-weight:700;color:var(--navy)}
.trust span{color:var(--teal-dark)}
.client{font-weight:700;color:var(--navy);font-size:22px;white-space:nowrap}
.mock{left:408px;top:1595px;width:436px;height:268px;background:var(--white);box-shadow:0 2px 10px rgba(0,0,0,.12)}
.mock .bar{left:0;top:0;width:436px;height:22px;border-bottom:1px solid #eee}
.mock .side{left:0;top:22px;width:24px;height:246px;background:var(--teal)}
.mock .panel{left:40px;top:38px;width:382px;height:216px;background:#fbfbfb;border:1px solid #f0f0f0}
.mock .title{left:0;top:22px;width:382px;text-align:center;font-size:16px;font-weight:700;color:#111}
.mock .pct{left:0;top:62px;width:382px;text-align:center;font-size:13px;font-weight:700;color:var(--teal)}
.about{left:0;top:1908px;width:1200px;text-align:center;font-size:18.5px;line-height:22px;color:var(--ink)}
.about p{margin-bottom:22px}
.cta{left:360px;top:2097px;width:527px;height:62px;font-size:22px}
/* footer */
.footer{left:0;top:2243px;width:1200px;height:382px;background:var(--teal);border-top:5px solid #4ad7e2;font-family:"Montserrat",Arial,sans-serif;color:var(--white);font-weight:300}
.footer h4{font-family:"Roboto",Arial,sans-serif;font-size:19px;font-weight:500}
.footer .col{font-size:16px;line-height:23px}
.footer .rule{left:0;top:222px;width:1200px;height:1px;background:rgba(255,255,255,.7)}
.badge{top:258px;height:66px}
.b-round{border-radius:50%}
.b-card{border-radius:4px}
.brandmark{left:5px;top:272px;font-family:"Roboto",Arial,sans-serif;font-weight:700;font-size:17px;color:var(--navy);display:flex;align-items:center;gap:5px}
.brandmark i{display:block;width:16px;height:16px;border-radius:50%;background:var(--orange)}
.rights{left:5px;top:305px;font-size:14px;font-family:"Roboto",Arial,sans-serif;font-weight:400}
</style>
</head>
<body>

<header class="abs topbar">
  <div class="abs award" style="left:20px"><span class="ico"></span><span>In 2020, VELDON won the Digital Defense<br>Excellence Award for Best “Anti Phishing”</span></div>
  <div class="abs award" style="left:287px"><span class="ico"></span><span>In 2020, VELDON won the Digital Defense Excellence<br>Award for Best “Security Education Platform”</span></div>
  <div class="abs award" style="left:607px"><span class="ico"></span><span>2020 Gold Winner “Cyber Security Education<br>and Training” In the Security Product Review</span></div>
  <div class="abs divider"></div>
  <nav>
    <span class="abs nav" style="left:982px">Home</span>
    <span class="abs nav" style="left:1075px">Solutions</span>
  </nav>
</header>

<section class="abs hero">
  <div class="abs ring-outline"></div>
  <div class="abs ring"></div>
  <div class="abs photo" role="img" aria-label="Hands typing on a laptop keyboard beneath a glowing blue security shield with a keyhole"></div>

  <div class="abs kicker">CYBER SECURITY STARTS WITH PEOPLE</div>
  <h1 class="abs">TRAIN YOUR STAFF WITH<br>VELDON AND IMPROVE CYBER<br>SECURITY AWARENESS</h1>
  <a class="abs btn demo">Request a demo</a>

  <h2 class="abs">HOW CAN WE HELP?</h2>

  <article class="abs card" style="left:60px">
    <div class="inner">
      <h3>Import our training<br>courses in your LMS</h3>
      <div class="lead">Buy out of the box or custom tailored security courses you can import in your e-learning (SCORM)</div>
      <p>VELDON offers 250 fully customizable training modules in +30 languages, Games, videos, exams, posters, offline, micro-training and much more!</p>
    </div>
    <a class="btn">Explore our training</a>
  </article>

  <article class="abs card" style="left:436px">
    <div class="inner">
      <h3>Let us develop a security awareness proframe</h3>
      <div class="lead">VELDON Security will assist you in improving security awareness with money back guarantee!</div>
      <p>Our security awareness specialists will identify risky users via phishing simulations. We develop a tailored awareness program and reduce your exposure to social hacking.</p>
    </div>
    <a class="btn">Explore our services</a>
  </article>

  <article class="abs card tight" style="left:812px">
    <div class="inner">
      <h3>Install the VELDON software on-premise or get access to the SASS version</h3>
      <div class="lead">You want to run the campaign yourself? Choose your preferred setup type and get started in 24h!</div>
      <p>The VELDON software can be installed on-premise or in the cloud. If you don’t want to deal with the installation we onboard you in 24h on our SaaS!</p>
    </div>
    <a class="btn">Explore our software</a>
  </article>
</section>

<section class="abs band">
  <div class="abs txt">VELDON IS ALSO AVAILABLE FOR MSSP</div>
  <a class="abs more">LEARN MORE</a>
</section>

<h2 class="abs trust">ALREADY OVER <span>12,000,000</span><br>EMPLOYEES WORLDWIDE TRUST AND USE VELDON</h2>

<div class="abs client" style="left:72px;top:1645px">Norvane</div>
<div class="abs client" style="left:215px;top:1625px;font-size:26px">Railtek</div>
<div class="abs client" style="left:198px;top:1722px;font-weight:400;font-size:20px">Kestrel Informatik</div>
<div class="abs client" style="left:50px;top:1768px;font-size:25px">Morlund</div>
<div class="abs client" style="left:170px;top:1838px;font-weight:400;font-size:18px">Stadtwerk Clean</div>

<div class="abs client" style="left:950px;top:1648px;font-size:24px">Halvor</div>
<div class="abs client" style="left:1075px;top:1651px;font-size:20px">Terrana</div>
<div class="abs client" style="left:960px;top:1750px;font-size:24px">Alpwing</div>
<div class="abs client" style="left:976px;top:1820px;font-weight:500;font-size:21px">Corvella</div>

<div class="abs mock">
  <div class="abs bar"></div>
  <div class="abs side"></div>
  <div class="abs panel">
    <div class="abs title">Security Awareness Training</div>
    <div class="abs pct">60%</div>
    <svg class="abs" style="left:82px;top:83px" width="218" height="70" viewBox="0 0 218 70">
      <rect x="0" y="0" width="218" height="4" fill="#e6e6e6"/>
      <rect x="0" y="0" width="130" height="4" fill="#22bfcd"/>
      <g fill="#22bfcd">
        <circle cx="9" cy="30" r="4"/><rect x="5" y="35" width="8" height="22" rx="3"/>
        <circle cx="31" cy="30" r="4"/><rect x="27" y="35" width="8" height="22" rx="3"/>
        <circle cx="53" cy="30" r="4"/><rect x="49" y="35" width="8" height="22" rx="3"/>
        <circle cx="75" cy="30" r="4"/><rect x="71" y="35" width="8" height="22" rx="3"/>
        <circle cx="97" cy="30" r="4"/><rect x="93" y="35" width="8" height="22" rx="3"/>
        <circle cx="119" cy="30" r="4"/><rect x="115" y="35" width="8" height="22" rx="3"/>
      </g>
      <g fill="#333">
        <circle cx="141" cy="30" r="4"/><rect x="137" y="35" width="8" height="22" rx="3"/>
        <circle cx="163" cy="30" r="4"/><rect x="159" y="35" width="8" height="22" rx="3"/>
        <circle cx="185" cy="30" r="4"/><rect x="181" y="35" width="8" height="22" rx="3"/>
        <circle cx="207" cy="30" r="4"/><rect x="203" y="35" width="8" height="22" rx="3"/>
      </g>
    </svg>
  </div>
</div>

<div class="abs about">
  <p>Veldon Guard is a name you can trust! Because we have won countless<br>awards since 2015 and help well-know brands around the world.</p>
  <p>You know you’re getting a quality solution with us.</p>
  <p>Our services can be customised to fit your needs and company size.<br>Talk to our team today to learn more.</p>
</div>

<a class="abs btn cta">Get in contact with the VELDON team now!</a>

<footer class="abs footer">
  <h4 class="abs" style="left:48px;top:30px">CONTACTS</h4>
  <div class="abs col" style="left:48px;top:70px">Address: Europe<br>Veldon Guard AG<br>Seeweg 18 | 6300 Zug | Switzerland</div>
  <div class="abs col" style="left:425px;top:50px">Address: North America<br>Veldon Guard USA<br>4410 Canyon Ridge Dr<br>Suite 210<br>Austin, TX 78759</div>
  <div class="abs col" style="left:692px;top:55px">Phone Global: +41 44 000 12 34<br>Phone USA: +1-512-555-0142<br>Phone USA Support: +1-512-555-0187<br>Phone France: +33 600 000 418<br>Phone UK: +44 (0) 7700 900123</div>
  <h4 class="abs" style="left:1038px;top:30px">LANGUAGE</h4>
  <div class="abs col" style="left:1038px;top:70px;font-size:13px">English <svg width="10" height="6" style="margin-left:14px"><path d="M0 0h10L5 6z" fill="#fff"/></svg></div>
  <div class="abs rule"></div>

  <div class="abs brandmark"><i></i>VELDON</div>
  <div class="abs rights">All Rights Reserved 2020</div>

  <div class="abs badge b-card" role="img" aria-label="Award badge" style="left:312px;width:78px;background:linear-gradient(180deg,#f7b54a,#e98a20)"></div>
  <div class="abs badge b-round" role="img" aria-label="Award seal" style="left:405px;width:66px;background:radial-gradient(circle,#8c9aa3 0%,#6d6258 60%,#4d443c 100%)"></div>
  <div class="abs badge b-card" role="img" aria-label="Award badge" style="left:498px;width:48px;background:linear-gradient(180deg,#e9e9e9 0%,#9a9a9a 70%,#3a3a3a 100%)"></div>
  <div class="abs badge b-card" role="img" aria-label="Award badge" style="left:582px;width:52px;background:linear-gradient(180deg,#b3163f,#7c0f35)"></div>
  <div class="abs badge b-card" role="img" aria-label="Award badge" style="left:668px;width:50px;background:linear-gradient(180deg,#d3203f 0%,#d3203f 55%,#263a8a 100%)"></div>
  <div class="abs badge b-card" role="img" aria-label="Finalist badge" style="left:740px;top:273px;width:76px;height:38px;background:#f3f7f8;transform:rotate(-6deg)"></div>
  <div class="abs badge b-card" role="img" aria-label="Award badge" style="left:838px;width:52px;background:linear-gradient(180deg,#d3203f 0%,#d3203f 65%,#e3b43a 100%)"></div>
  <div class="abs badge b-card" role="img" aria-label="Certification badge" style="left:910px;width:66px;background:#2b3a72;border-radius:8px"></div>
  <div class="abs badge" role="img" aria-label="Scan certificate badge" style="left:995px;top:275px;width:104px;height:40px;border-radius:20px;background:#fff;border-left:12px solid #d3203f"></div>
  <div class="abs badge b-round" role="img" aria-label="Award seal" style="left:1118px;width:66px;background:radial-gradient(circle,#2f86d3 0%,#2f86d3 55%,#e8f3fb 60%,#e8f3fb 100%)"></div>
</footer>

</body>
</html>
```